Flyer Design Project

Hi, I need a flyer designed for my Personal Training Studio. I have been doing early morning and afternoon appointments but am now able to offer appointments during the day. My Studio is situated on my property which is about 15mins drive from Orange at a small rural suburb called Borenore. My training sessions are completely private and I specialise on training individuals or two people. I already have a logo and a face book page under my trading name which is Kestrel Path Personal Training. I want the flyer for a letter box drop around my area to target new clients that would find my location convenient and the setting appealing.
Updates
Logo file is now attached.
Target Market(s)
Local people close to my area
Industry/Entity Type
Training
Requirements
Must have
- Logo (attached)

```html
<!DOCTYPE html>
<html lang="en">
<head>
<meta charset="utf-8">
<title>Kestrel Path Personal Training Flyer</title>
<link href="https://fonts.googleapis.com/css2?family=Open+Sans:wght@400;700;800&display=swap" rel="stylesheet">
<style>
  :root {
    --band-red: #7a1a0c;
    --band-dark: #3a0904;
    --photo-red: #b8402a;
    --photo-dark: #2a0603;
    --ink-white: #ffffff;
    --silver-light: #ffffff;
    --silver-dark: #9a9a9a;
    --mark-blue: #1f5fe0;
  }
  html, body {
    margin: 0;
    padding: 0;
    overflow: hidden;
    background: #222;
  }
  .flyer {
    position: relative;
    width: 1200px;
    height: 2522px;
    overflow: hidden;
    font-family: "Open Sans", Arial, sans-serif;
    color: var(--ink-white);
    background: var(--band-dark);
  }
  .top-band {
    position: absolute;
    left: 0; top: 0;
    width: 1200px; height: 694px;
    background: radial-gradient(ellipse at 50% 40%, var(--band-red) 0%, #5a1208 60%, var(--band-dark) 100%);
    border-bottom: 6px solid #1a0301;
    box-shadow: 0 10px 24px rgba(0,0,0,0.7);
    z-index: 2;
  }
  .hero-photo {
    position: absolute;
    left: 0; top: 700px;
    width: 1200px; height: 1822px;
    background: radial-gradient(ellipse 65% 55% at 50% 35%, var(--photo-red) 0%, #8a2816 45%, #4a0e06 80%, var(--photo-dark) 100%);
  }
  .main-contact {
    position: absolute;
    top: 128px; left: 0; width: 1200px;
    text-align: center;
    font-size: 59px;
    font-weight: 400;
    z-index: 3;
  }
  .brand {
    position: absolute;
    top: 294px; left: 148px;
    display: flex;
    align-items: center;
    gap: 36px;
    z-index: 3;
  }
  .brand-dot {
    width: 270px; height: 270px;
    border-radius: 50%;
    background: var(--mark-blue);
    flex: none;
  }
  .brand-name {
    font-size: 70px;
    font-weight: 700;
    line-height: 1.15;
    color: var(--ink-white);
  }
  .headline {
    position: absolute;
    top: 752px; left: 0; width: 1200px;
    margin: 0;
    text-align: center;
    font-size: 178px;
    font-weight: 800;
    line-height: 0.98;
    letter-spacing: 2px;
    color: var(--silver-light);
    background: linear-gradient(180deg, var(--silver-light) 10%, #d8d8d8 50%, var(--silver-dark) 100%);
    -webkit-background-clip: text;
    background-clip: text;
    -webkit-text-fill-color: transparent;
    filter: drop-shadow(6px 8px 4px rgba(0,0,0,0.75));
  }
  .body-copy {
    position: absolute;
    left: 63px; width: 1082px;
    margin: 0;
    font-size: 38px;
    line-height: 50px;
    text-align: justify;
    text-shadow: 2px 2px 3px rgba(0,0,0,0.6);
  }
  .body-copy.first { top: 1146px; }
  .body-copy.second { top: 1656px; }
  .contact {
    position: absolute;
    top: 1998px; left: 0; width: 1200px;
    text-align: center;
    text-shadow: 2px 2px 3px rgba(0,0,0,0.6);
  }
  .contact-title {
    font-size: 59px;
    font-weight: 700;
    line-height: 76px;
    margin-bottom: 6px;
  }
  .contact-line {
    font-size: 60px;
    line-height: 77px;
  }
  .website {
    position: absolute;
    top: 2396px; left: 0; width: 1200px;
    text-align: center;
    font-size: 82px;
    font-weight: 400;
    text-shadow: 2px 2px 3px rgba(0,0,0,0.6);
  }
</style>
</head>
<body>
<div class="flyer">
  <div class="top-band"></div>
  <div class="hero-photo" role="img" aria-label="Photograph of a muscular trainer's bare torso with clenched fists on a red background"></div>

  <div class="main-contact">Private studio in Borenore</div>

  <div class="brand">
    <div class="brand-dot"></div>
    <div class="brand-name">Kestrel Path<br>Personal Training</div>
  </div>

  <h1 class="headline">NOW OPEN<br>ALL DAY</h1>

  <p class="body-copy first">Great news for locals: as well as my early morning and afternoon appointments, I can now offer training sessions right through the day. Whether you work shifts, have free time during school hours or simply prefer to train at midday, there is now a time that suits you. Every session is completely private and built around your goals, your fitness level and your pace, so you get my full attention from the first warm up to the last stretch.</p>

  <p class="body-copy second">My studio sits on my own property in the quiet rural suburb of Borenore, only about 15 minutes drive from Orange. Enjoy easy parking, fresh country air and a calm, welcoming setting with no crowded gym floor and no waiting for equipment. Train one on one, or bring a partner along and stay motivated together.</p>

  <div class="contact">
    <div class="contact-title">Book your session</div>
    <div class="contact-line">Mornings and afternoons</div>
    <div class="contact-line">Now daytimes too</div>
    <div class="contact-line">Just 15 mins from Orange</div>
  </div>

  <div class="website">www.yourwebpage.com</div>
</div>
</body>
</html>
```